Awesome photographers card for an awesome new business

Double sided business card Black background and silver logo in middle on one side. Details on otherside. please keep it simple

Photographer

Gavin Tolley
0482615073
GavinTolleyPhotography82@lumenpost.com
www.GavinTolleyPhotography.com.au
Instagram _Gavin_tolley

Requirements
Must have
• My logo in Silver
• please use instagram logo instead of "Instagram"

```html
<!DOCTYPE html>
<html lang="en">
<head>
<meta charset="utf-8">
<title>Gavin Tolley Photography – Business Card</title>
<link rel="stylesheet" href="https://fonts.googleapis.com/css2?family=Open+Sans:wght@400;600;700&display=swap">
<style>
  :root{
    --stage:#e9e7e4;
    --card-black:#232323;
    --card-black-deep:#1b1b1b;
    --silver:#d9d9d9;
    --silver-dark:#9a9a9a;
    --band-white:#f4f4f4;
    --band-grey:#c9c9c9;
    --text-light:#ececec;
  }
  *{margin:0;padding:0;box-sizing:border-box}
  html,body{width:1200px;height:900px;overflow:hidden}
  body{background:var(--stage);font-family:"Open Sans",Arial,sans-serif;position:relative}

  .card{position:absolute;left:280px;width:640px;height:360px;overflow:hidden;
        box-shadow:0 6px 18px rgba(0,0,0,.18)}
  .card--front{top:50px;
        background:repeating-linear-gradient(0deg,var(--card-black) 0 2px,var(--card-black-deep) 2px 4px)}
  .card--back{top:470px;background:var(--card-black)}

  .brand{position:absolute;display:flex;align-items:center;gap:12px;color:var(--silver)}
  .brand__dot{width:58px;height:58px;border-radius:50%;border:3px solid var(--silver);flex:none}
  .brand__name{font-weight:600;font-size:17px;letter-spacing:.18em;text-transform:uppercase;line-height:1.35}
  .card--front .brand{left:50%;top:50%;transform:translate(-50%,-50%)}
  .card--back .brand{right:44px;top:170px}
  .card--back .brand__dot{width:48px;height:48px}
  .card--back .brand__name{font-size:14px}

  .holder{position:absolute;left:0;top:22px;display:flex;align-items:center;gap:22px}
  .holder__tab{width:70px;height:40px;display:block}
  .holder__name{font-weight:700;font-size:21px;color:var(--silver)}

  .contacts{position:absolute;left:40px;top:150px;list-style:none}
  .contacts li{display:flex;align-items:center;gap:12px;color:var(--text-light);font-size:15px;line-height:25px}
  .contacts svg{width:13px;height:13px;flex:none}
  .contacts .square{width:11px;height:11px;background:var(--silver);flex:none;margin:0 1px}

  .footer-band{position:absolute;left:0;bottom:0;width:640px;height:70px}
</style>
</head>
<body>

<section class="card card--front" aria-label="Card front">
  <div class="brand">
    <span class="brand__dot"></span>
    <span class="brand__name">Gavin Tolley<br>Photography</span>
  </div>
</section>

<section class="card card--back" aria-label="Card back">
  <div class="holder">
    <svg class="holder__tab" viewBox="0 0 70 40" aria-hidden="true">
      <defs>
        <linearGradient id="silverTab" x1="0" y1="0" x2="1" y2="1">
          <stop offset="0" stop-color="#f2f2f2"/><stop offset="1" stop-color="#8d8d8d"/>
        </linearGradient>
      </defs>
      <polygon points="0,0 46,0 24,40 0,40" fill="url(#silverTab)"/>
      <polygon points="50,0 70,0 70,40 28,40" fill="url(#silverTab)"/>
    </svg>
    <h1 class="holder__name">Gavin Tolley</h1>
  </div>

  <ul class="contacts">
    <li><svg viewBox="0 0 24 24" aria-hidden="true"><path fill="#ddd" d="M6.6 10.8a15 15 0 0 0 6.6 6.6l2.2-2.2c.3-.3.7-.4 1-.2 1.1.4 2.3.6 3.6.6.6 0 1 .4 1 1V20c0 .6-.4 1-1 1A17 17 0 0 1 3 4c0-.6.4-1 1-1h3.5c.6 0 1 .4 1 1 0 1.3.2 2.5.6 3.6.1.3 0 .7-.2 1z"/></svg>0482615073</li>
    <li><svg viewBox="0 0 24 24" aria-hidden="true"><rect x="2" y="5" width="20" height="14" fill="#ddd"/><path d="M2 5l10 8 10-8" fill="none" stroke="#232323" stroke-width="2"/></svg>GavinTolleyPhotography82@lumenpost.com</li>
    <li><svg viewBox="0 0 24 24" aria-hidden="true"><circle cx="12" cy="12" r="10" fill="#ddd"/><path d="M2 12h20M12 2c3 3 3 17 0 20M12 2c-3 3-3 17 0 20" fill="none" stroke="#232323" stroke-width="1.5"/></svg>www.GavinTolleyPhotography.com.au</li>
    <li><span class="square"></span>_Gavin_tolley</li>
  </ul>

  <svg class="footer-band" viewBox="0 0 640 70" preserveAspectRatio="none" aria-hidden="true">
    <defs>
      <linearGradient id="bandFade" x1="0" y1="0" x2="1" y2="0">
        <stop offset="0" stop-color="#fafafa"/><stop offset="1" stop-color="#d6d6d6"/>
      </linearGradient>
    </defs>
    <rect x="0" y="40" width="640" height="30" fill="url(#bandFade)"/>
    <polygon points="0,12 250,12 235,40 0,40" fill="#f4f4f4"/>
    <polygon points="256,12 272,12 257,40 241,40" fill="#111"/>
    <polygon points="278,12 640,12 640,40 263,40" fill="url(#bandFade)"/>
  </svg>

  <div class="brand">
    <span class="brand__dot"></span>
    <span class="brand__name">Gavin Tolley<br>Photography</span>
  </div>
</section>

</body>
</html>
```